Vice chair

I'm running for a position as vice chair this will be posted in the lunch room cafeteria in this package i posted logos, my picture, sample of old flyers to give you a idea i also wrote literature need help in putting it together like it to look like a million bucks goal win this election I summited lots of pdf files and jpeg look though them to help with your design feel free to contact me to further assist you
Updates

Would like this to be completed by Wednesday

Target Market(s)

My constituents

Font styles to use
Serif

Colors

Designer to choose colors to be used in the design.

Requirements
Must have
• Make it look clean neat
Nice to have
• Nice background

```html
<!DOCTYPE html>
<html lang="en">
<head>
<meta charset="utf-8">
<title>Danny Morales for Vice Chair</title>
<link href="https://fonts.googleapis.com/css2?family=Oswald:wght@400;500;600;700&family=Open+Sans:ital,wght@0,400;0,600;0,700;1,400;1,600&family=Montserrat:wght@700;800&family=Pacifico&display=swap" rel="stylesheet">
<style>
  :root{
    --red:#e21d26;
    --black:#141414;
    --ink:#444;
    --white:#ffffff;
    --pink:#fde3e3;
    --navy:#1c2a5e;
    --gold:#f7b515;
    --page:#e9e9e9;
  }
  *{box-sizing:border-box;margin:0;padding:0}
  html,body{width:1200px;height:900px;overflow:hidden;background:var(--page)}
  .flyer{position:absolute;left:296px;top:20px;width:608px;height:860px;background:var(--white);overflow:hidden;box-shadow:0 4px 14px rgba(0,0,0,.25);font-family:"Open Sans",sans-serif}
  .abs{position:absolute}

  /* hero */
  .hero{left:0;top:0;width:608px;height:342px;background:linear-gradient(115deg,#22306a 0%,#3b3f7a 22%,#c9322c 45%,#e8562a 62%,#f08a3a 75%,#d8312a 100%)}
  .portrait{left:0;top:24px;width:222px;height:318px;background:linear-gradient(180deg,#8a6450 0%,#5e4437 45%,#1e1a19 75%,#161414 100%);border-radius:90px 90px 0 0}
  .first-name{left:250px;top:22px;font-family:"Montserrat",sans-serif;font-weight:800;font-size:34px;color:var(--white);letter-spacing:1px}
  .last-name{left:239px;top:53px;width:301px;height:76px;background:var(--red);color:var(--white);font-family:"Oswald",sans-serif;font-weight:600;font-size:60px;letter-spacing:6px;line-height:76px;text-align:center}
  .tagline{left:305px;top:130px;width:222px;height:34px;background:var(--pink);color:var(--red);font-family:"Oswald",sans-serif;font-weight:500;font-size:25px;letter-spacing:2px;line-height:34px;text-align:center}
  .tagline .small{font-family:Georgia,serif;font-style:italic;font-size:14px;color:var(--navy);letter-spacing:0;text-decoration:underline}
  .badge{border-radius:50%;border:4px solid var(--black)}
  .badge-one{left:209px;top:199px;width:128px;height:128px;background:radial-gradient(circle,#f3c63a 0 55%,#e8502a 56% 100%)}
  .badge-two{left:342px;top:168px;width:128px;height:128px;background:radial-gradient(circle,#dfe9f6 0 55%,#1e4fa3 56% 100%)}
  .badge-three{left:458px;top:235px;width:128px;height:128px;background:radial-gradient(circle,#f7e33a 0 55%,#d92a2a 56% 60%,#f7e33a 61% 100%)}

  /* slate band */
  .band{left:0;top:342px;width:608px;height:186px}
  .band-photo{left:0;top:0;width:608px;height:186px;background:linear-gradient(90deg,#1a1a1a 40%,#2c2c2c 70%,#3a3a3a 100%)}
  .respect{left:25px;top:12px;color:var(--white);font-style:italic;font-weight:600;font-size:14px;line-height:1}
  .integrity{left:25px;top:24px;color:var(--white);font-family:"Montserrat",sans-serif;font-weight:800;font-size:22px}
  .backbone{left:25px;top:50px;color:#ffd5d5;font-size:7.5px}
  .backbone b{color:var(--white)}
  .record{left:25px;top:68px;width:300px;color:var(--white);font-size:12.5px;line-height:1.3}
  .note{left:25px;top:140px;width:310px;color:var(--white);font-style:italic;font-size:9px;line-height:1.3}
  .slate{left:366px;top:22px;color:var(--red);font-family:"Oswald",sans-serif;font-weight:600;font-size:38px;letter-spacing:1px;white-space:nowrap}
  .slate .the{font-family:"Pacifico",cursive;font-size:22px;color:var(--white);font-weight:400}
  .years{left:352px;top:86px;width:78px;height:78px;border-radius:50%;background:var(--white);border:3px solid #cfcfcf;text-align:center;font-family:"Oswald",sans-serif;line-height:1}
  .years .num{display:block;color:var(--red);font-size:24px;font-weight:700;margin-top:11px}
  .years .word{display:block;color:var(--red);font-size:11px;font-weight:600}
  .years .job{display:block;color:var(--navy);font-size:9px}
  .ballot{left:471px;top:81px;width:63px;height:62px;border:3px solid var(--red);color:var(--white);font-family:"Montserrat",sans-serif;font-weight:700;font-size:52px;line-height:56px;text-align:center}

  /* intro */
  .intro{left:0;top:528px;width:608px;height:200px;background:linear-gradient(90deg,#f4f4f4 0%,#ececec 45%,#e3e3e3 100%)}
  .mission-art{left:13px;top:13px;width:178px;height:178px;border-radius:50%;background:radial-gradient(circle at 45% 45%,#f9c233 0%,var(--gold) 70%,#eda90f 100%)}
  .intro-copy{left:232px;top:45px;width:358px;color:var(--ink);font-size:8.3px;line-height:1.25}
  .intro-copy p{margin-bottom:10px}
  .intro-copy .name{color:var(--red);font-weight:600;font-size:10px}
  .intro-copy .ask{color:var(--red);font-style:italic;font-weight:600;font-size:9.5px}

  /* closing */
  .closing{left:0;top:728px;width:608px;height:73px;background:var(--black);text-align:center;padding:11px 20px 0}
  .closing h2{color:var(--red);font-family:"Oswald",sans-serif;font-weight:600;font-size:11.5px;letter-spacing:.3px}
  .closing p{color:var(--white);font-style:italic;font-size:11px;line-height:1.5;margin-top:2px}

  /* footer */
  .footer{left:0;top:801px;width:608px;height:59px;background:var(--red);color:var(--white);font-family:"Oswald",sans-serif;display:flex;align-items:center;justify-content:center;gap:14px;white-space:nowrap}
  .footer .big{font-weight:600;font-size:30px}
  .footer .mid{font-weight:400;font-size:23px;margin-right:12px}
</style>
</head>
<body>
<main class="flyer">
  <section class="hero abs" role="img" aria-label="Waving American flag background">
    <div class="portrait abs" role="img" aria-label="Portrait photo of the candidate"></div>
    <div class="first-name abs">DANNY</div>
    <h1 class="last-name abs">MORALES</h1>
    <div class="tagline abs">TIME <span class="small">for</span> CHANGE</div>
    <div class="badge badge-one abs" role="img" aria-label="Depot badge"></div>
    <div class="badge badge-two abs" role="img" aria-label="Depot badge"></div>
    <div class="badge badge-three abs" role="img" aria-label="Depot badge"></div>
  </section>

  <section class="band abs">
    <div class="band-photo abs" role="img" aria-label="Buses parked at the depot"></div>
    <svg class="abs" width="608" height="186" style="left:0;top:0">
      <polygon points="0,0 277,0 444,186 0,186" fill="var(--red)"/>
    </svg>
    <div class="respect abs">Respect &amp;</div>
    <div class="integrity abs">INTEGRITY</div>
    <div class="backbone abs">Metro Riders Union will be the <b>BACKBONE</b> that shapes our union</div>
    <p class="record abs">Past union member of freight workers local 412 believes in There is a collective bargainning agreement in place and no management is above the law to violate it.</p>
    <p class="note abs">Past union member of freight workers local 907 believes a house that is divided cannot stand alone</p>
    <div class="slate abs">VOTE <span class="the">the</span> SLATE</div>
    <div class="years abs"><span class="num">20</span><span class="word">YEARS</span><span class="job">ON THE JOB</span></div>
    <div class="ballot abs">X</div>
  </section>

  <section class="intro abs">
    <div class="mission-art abs" role="img" aria-label="Vote with your mission badge artwork with a ballot sign"></div>
    <div class="intro-copy abs">
      <p>I <span class="name">danny Morales</span> for those who don't know me would like to introduce myself i have always been approchable and helpful whether you are a probationary officer or a veteran operator with knowledge or information. we must protect our union rules for ourselves our future and most important our children.</p>
      <p>i would like this opportunity to run as your vice chair a person you can trust and believe in me positive and motivations are my main keys for progress and for change in my campaingn when thereare no leders to look up to one therefore must become one i do believe i'm the right person for this position so.</p>
      <p class="ask">Please come out and support me and vote me as your vice chair.</p>
    </div>
  </section>

  <section class="closing abs">
    <h2>IN CLOSING I BELIEVE THAT OUR UNION DOES NOT STAND OUT INDIVIDUALLY ACHIEVEMENT FOR ALL</h2>
    <p>we must always continue to stand together, stay together &amp; fight together so we can win together because<br>success is never owned, it is rented and the rent is due every day.</p>
  </section>

  <footer class="footer abs">
    <span class="big">VOTE</span>
    <span class="mid">independent me as your</span>
    <span class="big">VICE CHAIR</span>
  </footer>
</main>
</body>
</html>
```